Fernhollow Coldbrew concept

Web site/logo for Fernhollow Coldbrew served in a keg tap. Fernhollow Coldbrew is a natural energy beverage roasted with fair trade/organic beans. Based in New England. Think- Fresh, Natural, Organic, Pure, Mills, Brick, Wood. Fernhollow Coldbrew.

Target Market(s)

Individuals looking for energy drinks without added sugar or dairy. Coffee connoisseurs.

Industry/Entity Type

Trade

Logo Text

Fernhollow Coldbrew

Number of Pages Required

1 page

Font styles to use
Serif

```html
<!DOCTYPE html>
<html lang="en">
<head>
<meta charset="utf-8">
<title>Fernhollow Coldbrew</title>
<link href="https://fonts.googleapis.com/css2?family=Fira+Sans:ital,wght@0,400;0,500;0,600;0,700;1,700&family=Lato:wght@400;700&display=swap" rel="stylesheet">
<style>
:root{
  --espresso:#4a1e08;
  --roast:#5a2a0e;
  --rust:#6b3410;
  --caramel:#8a5a30;
  --sand:#d8c9a0;
  --cream:#f0e0a8;
  --paper:#e4ddcc;
  --ink:#2b1a10;
  --white:#ffffff;
  --field:#bdb6a6;
}
*{box-sizing:border-box;margin:0;padding:0}
html,body{width:1200px;height:2601px;overflow:hidden}
body{font-family:"Lato",sans-serif;background:var(--white);color:var(--ink);position:relative}
.abs{position:absolute}
.pill{display:inline-block;border-radius:20px;font-family:"Fira Sans",sans-serif;font-style:italic;font-weight:700;font-size:15px;letter-spacing:1px;padding:8px 20px;text-transform:uppercase}

/* hero */
.hero{position:absolute;left:0;top:0;width:1200px;height:682px;background:var(--white);overflow:hidden}
.hero-band{position:absolute;left:0;top:0;width:1200px;height:330px;background:linear-gradient(90deg,#3a1a0a,#6a3a1c 40%,#3c1c0c 70%,#5a3018);clip-path:polygon(0 0,100% 0,100% 84%,0 100%)}
.hero-photo{position:absolute;left:0;top:0;width:510px;height:682px;background:linear-gradient(180deg,#3a1a0a 0%,#b8b2aa 45%,#e8e4de 70%,#f4f2ee 100%)}
.topbar{position:absolute;top:24px;left:0;width:1200px;height:30px;color:var(--white);font-size:14px}
.topbar .phone{left:86px;top:4px;display:flex;align-items:center;gap:10px}
.topbar .mail{right:80px;top:4px;display:flex;align-items:center;gap:10px}
.ico-round{width:28px;height:28px;border-radius:50%;background:rgba(255,255,255,.25);display:flex;align-items:center;justify-content:center}
.nav{position:absolute;left:0;top:76px;width:1200px;height:70px;background:linear-gradient(180deg,#7a4218,#5a2a0e);border-top:1px dashed rgba(240,224,168,.5);border-bottom:1px dashed rgba(240,224,168,.5)}
.nav a{position:absolute;top:24px;color:var(--white);font-family:"Fira Sans",sans-serif;font-weight:600;font-size:15px;text-decoration:none;letter-spacing:.3px}
.nav a.active{color:var(--cream)}
.nav .social{position:absolute;top:27px;width:16px;height:16px;border-radius:50%;border:2px solid var(--white)}
.brand{position:absolute;left:489px;top:14px;width:196px;height:196px;border-radius:50%;background:var(--roast);border:4px solid #7a4218;box-shadow:0 0 0 2px rgba(240,224,168,.5) inset;display:flex;flex-direction:column;align-items:center;justify-content:center;color:var(--cream);font-family:"Fira Sans",sans-serif;font-weight:700;font-size:22px;line-height:1.25;letter-spacing:.5px;text-align:center}
.hero-title{position:absolute;right:80px;top:362px;width:620px;text-align:right;font-family:"Fira Sans",sans-serif;font-weight:500;font-size:36px;line-height:1.38;color:var(--rust)}
.dots{position:absolute;right:78px;top:548px;display:flex;gap:8px}
.dots span{width:17px;height:17px;border-radius:50%;background:var(--cream)}
.dots span:first-child{background:var(--roast)}

/* benefits */
.benefits{position:absolute;left:0;top:682px;width:1200px;height:397px;background:var(--sand)}
.benefit{position:absolute;top:58px;width:250px;text-align:center}
.badge{width:124px;height:124px;border-radius:50%;background:var(--roast);margin:0 auto;display:flex;align-items:center;justify-content:center;box-shadow:0 0 0 5px rgba(90,42,14,.25)}
.badge-inner{width:108px;height:108px;border-radius:50%;border:2px dashed var(--cream);display:flex;align-items:center;justify-content:center}
.benefit h3{margin-top:20px;font-family:"Fira Sans",sans-serif;font-weight:600;font-size:22px;line-height:1.2;color:var(--roast)}
.benefits .pill{position:absolute;left:535px;top:304px;background:var(--roast);color:var(--white)}

/* about */
.about{position:absolute;left:0;top:1079px;width:1200px;height:421px}
.about-copy{position:absolute;left:0;top:0;width:600px;height:421px;background:linear-gradient(135deg,#946238,#7c4e28);padding:48px 82px 0 86px;color:var(--white)}
.about-copy h2{font-family:"Fira Sans",sans-serif;font-style:italic;font-weight:700;font-size:34px;letter-spacing:.3px;padding-bottom:14px;border-bottom:1px solid rgba(255,255,255,.5);margin-bottom:20px}
.about-copy p{font-size:14.6px;line-height:1.55;text-align:justify}
.about-copy .pill{margin-top:30px;border:2px solid var(--white);color:var(--white);padding:6px 18px}
.about-photo{position:absolute;left:600px;top:0;width:600px;height:421px;background:linear-gradient(160deg,#6a4a34,#3a2a28 50%,#8a6a58)}
.play{position:absolute;left:262px;top:168px}

/* steps */
.steps{position:absolute;left:0;top:1500px;width:1200px;height:342px;background:linear-gradient(180deg,#6b5238,#4c3a26)}
.step{position:absolute;top:56px;width:300px;text-align:center;color:var(--white)}
.step .badge{width:120px;height:120px;background:var(--rust);box-shadow:0 0 0 3px rgba(240,224,168,.25)}
.step .badge-inner{width:104px;height:104px}
.step h3{margin-top:26px;font-family:"Fira Sans",sans-serif;font-weight:600;font-size:22px;color:var(--cream)}
.step p{margin-top:10px;font-size:14px;line-height:1.3}

/* keg */
.keg{position:absolute;left:0;top:1842px;width:1200px;height:401px}
.keg-photo{position:absolute;left:0;top:0;width:468px;height:401px;background:linear-gradient(150deg,#7a8a84,#3a3a36 55%,#1e4a2a)}
.keg-beans{position:absolute;left:468px;top:0;width:732px;height:401px;background:radial-gradient(ellipse at center,#3a1a0c,#1e0c04)}
.keg-copy{position:absolute;left:468px;top:80px;width:732px;text-align:center;color:var(--white);font-family:"Fira Sans",sans-serif}
.keg-copy .kicker{font-weight:500;font-size:33px;letter-spacing:1.5px;display:flex;align-items:center;justify-content:center;gap:22px}
.keg-copy .kicker::before,.keg-copy .kicker::after{content:"";width:150px;height:1px;background:rgba(255,255,255,.45)}
.keg-copy h2{font-style:italic;font-weight:700;font-size:62px;letter-spacing:2px;color:var(--cream);line-height:1.15;margin-top:4px}
.keg-copy .sub{font-weight:600;font-size:33px;margin-top:4px}
.keg-copy .pill{margin-top:22px;background:var(--cream);color:var(--roast);padding:7px 22px}

/* footer */
.footer{position:absolute;left:0;top:2243px;width:1200px;height:287px;background:var(--paper)}
.col{position:absolute;top:46px}
.col h4{font-family:"Fira Sans",sans-serif;font-weight:600;font-size:15px;color:var(--ink);padding-bottom:10px;position:relative;margin-bottom:16px}
.col h4::after{content:"";position:absolute;left:0;bottom:0;width:38px;height:2px;background:var(--rust)}
.links li{list-style:none;font-size:13.5px;margin-bottom:14px;color:var(--ink)}
.links li::before{content:"›";margin-right:6px;font-weight:700}
.field{width:202px;height:30px;background:var(--field);margin-bottom:9px;color:#ece8e0;font-size:11px;padding:8px 6px}
.submit{display:inline-block;margin-top:8px;background:var(--espresso);color:var(--white);border-radius:16px;padding:6px 18px;font-family:"Fira Sans",sans-serif;font-style:italic;font-weight:700;font-size:13px;letter-spacing:1px}
.contact-row{display:flex;gap:10px;font-size:13px;line-height:1.4;margin-bottom:12px;align-items:flex-start}
.contact-row svg{flex:none;margin-top:2px}
.map{width:232px;height:140px;background:linear-gradient(135deg,#c8d8e4,#9ab8cc 50%,#d4dcc4);border:3px solid var(--white)}

.copyright{position:absolute;left:0;top:2530px;width:1200px;height:71px;background:var(--espresso);color:#e8d8c0;font-size:13px}
.copyright p{position:absolute;left:84px;top:28px}
.copyright .social{position:absolute;top:22px;width:30px;height:30px;border-radius:50%;border:2px solid var(--white)}
</style>
</head>
<body>

<header class="hero">
  <div class="hero-photo" role="img" aria-label="Cold brew coffee pouring from a keg tap into a glass"></div>
  <div class="hero-band" role="img" aria-label="Row of chrome beer taps on a wooden bar"></div>

  <div class="topbar">
    <div class="abs phone"><span class="ico-round"><svg width="14" height="14" viewBox="0 0 24 24"><path d="M6.6 10.8a15 15 0 0 0 6.6 6.6l2.2-2.2c.3-.3.7-.4 1-.2 1.1.4 2.3.6 3.6.6.6 0 1 .4 1 1V20c0 .6-.4 1-1 1A17 17 0 0 1 3 4c0-.6.4-1 1-1h3.5c.6 0 1 .4 1 1 0 1.3.2 2.5.6 3.6.1.3 0 .7-.2 1z" fill="#fff"/></svg></span>555 - 018 - 2046</div>
    <div class="abs mail"><span class="ico-round"><svg width="14" height="14" viewBox="0 0 24 24"><rect x="3" y="6" width="18" height="12" fill="none" stroke="#fff" stroke-width="2"/><path d="M3 6l9 7 9-7" fill="none" stroke="#fff" stroke-width="2"/></svg></span>info@fernhollowcoldbrew.com</div>
  </div>

  <nav class="nav">
    <a class="active" style="left:86px">HOME</a>
    <a style="left:212px">ABOUT</a>
    <a style="left:346px">PRODUCTS</a>
    <a style="left:729px">HEALTH BENEFITS</a>
    <a style="left:900px">CONTACT US</a>
    <span class="social" style="left:1068px"></span>
    <span class="social" style="left:1104px"></span>
  </nav>

  <div class="brand">FERNHOLLOW<br>COLDBREW</div>

  <h1 class="hero-title">Our Cold Brew Coffee Is A Natural Energy Beverage Roasted With Fair Trade/organic&nbsp; Beans</h1>
  <div class="dots"><span></span><span></span><span></span></div>
</header>

<section class="benefits">
  <div class="benefit" style="left:101px">
    <div class="badge"><div class="badge-inner"><svg width="56" height="56" viewBox="0 0 56 56" fill="none" stroke="#f0e0a8" stroke-width="2.5"><polygon points="28,6 40,13 40,27 28,34 16,27 16,13"/><polygon points="16,27 28,34 28,48 16,55 4,48 4,34" transform="translate(0,-6)"/><polygon points="40,27 52,34 52,48 40,55 28,48 28,34" transform="translate(0,-6)"/></svg></div></div>
    <h3>High in<br>Antioxidants</h3>
  </div>
  <div class="benefit" style="left:353px">
    <div class="badge"><div class="badge-inner"><svg width="56" height="56" viewBox="0 0 56 56" fill="#f0e0a8"><path d="M24 10c-9 0-15 6-15 14 0 4 1 6 3 8v14h16v-6h5c2 0 3-1 3-3v-5h4l-4-8c0-8-5-14-12-14z"/><rect x="40" y="10" width="4" height="16"/><rect x="34" y="16" width="16" height="4"/></svg></div></div>
    <h3>Improves Mental &amp;<br>Physical Performance</h3>
  </div>
  <div class="benefit" style="left:601px">
    <div class="badge"><div class="badge-inner"><svg width="56" height="56" viewBox="0 0 56 56" fill="none" stroke="#f0e0a8" stroke-width="3"><circle cx="28" cy="28" r="22"/><path d="M28 16l11 6v12l-11 6-11-6V22z" fill="#f0e0a8" stroke="none"/><path d="M17 22l11 6 11-6M28 28v12" stroke="#5a2a0e" stroke-width="2"/></svg></div></div>
    <h3>Doesn’t<br>Need Sugar</h3>
  </div>
  <div class="benefit" style="left:853px">
    <div class="badge"><div class="badge-inner"><svg width="56" height="56" viewBox="0 0 56 56" fill="none" stroke="#f0e0a8" stroke-width="3"><rect x="12" y="10" width="32" height="40" rx="2"/><rect x="21" y="6" width="14" height="8" fill="#f0e0a8"/><path d="M18 24l3 3 5-5M30 25h8M18 36l3 3 5-5M30 37h8" stroke-width="2.5"/></svg></div></div>
    <h3>Lower in<br>Acidity</h3>
  </div>
  <span class="pill">Read More</span>
</section>

<section class="about">
  <div class="about-copy">
    <h2>ABOUT COLD BREW COFFEE</h2>
    <p>Lorem ipsum dolor sit amet, consectetuer adipiscing elit, sed diam nonummy nibh euismod tincidunt ut laoreet dolore magna aliquam erat volutpat. Ut wisi enim ad minim veniam, quis nostrud exerci tation ullamcorper suscipit lobortis nisl ut aliquip ex ea commodo consequat. Duis autem vel eum iriure dolor in hendrerit in vulputate velit esse molestie consequat, vel illum dolore eu feugiat nulla facilisis at vero eros et accumsan et iusto odio dignissim qui blandit praesent luptatum zzril delenit augue duis dolore te feugait nulla facilisi accumsan et iusto odio.</p>
    <span class="pill">Read More</span>
  </div>
  <div class="about-photo" role="img" aria-label="Two friends raising glasses of cold brew coffee in a café">
    <svg class="play" width="74" height="74" viewBox="0 0 74 74"><circle cx="37" cy="37" r="34" fill="rgba(0,0,0,.15)" stroke="#fff" stroke-width="3"/><path d="M30 23l22 14-22 14z" fill="#fff"/></svg>
  </div>
</section>

<section class="steps">
  <div class="step" style="left:86px">
    <div class="badge"><div class="badge-inner"><svg width="52" height="52" viewBox="0 0 52 52" fill="none" stroke="#f0e0a8" stroke-width="3"><rect x="12" y="14" width="24" height="26" rx="3" transform="rotate(-35 24 27)"/><path d="M16 22l14 14M20 18l14 14" stroke-width="2"/></svg></div></div>
    <h3>STEP ONE: BREW</h3>
    <p>Lorem ipsum dolor sit amet, consectetuer adipiscing elit, sed diam nonummy nibh euismod tincidunt ut laoreet dolore magna aliquam erat</p>
  </div>
  <div class="step" style="left:450px">
    <div class="badge"><div class="badge-inner"><svg width="52" height="52" viewBox="0 0 52 52" fill="#f0e0a8"><path d="M20 8a4 4 0 0 1 8 0v14l10 3c3 1 4 3 4 6l-2 15H20l-8-14c-1-2 0-4 2-4s3 1 4 2l2 3z"/></svg></div></div>
    <h3>STEP TWO: TAP</h3>
    <p>Lorem ipsum dolor sit amet, consectetuer adipiscing elit, sed diam nonummy nibh euismod tincidunt ut laoreet dolore magna aliquam erat</p>
  </div>
  <div class="step" style="left:811px">
    <div class="badge"><div class="badge-inner"><svg width="52" height="52" viewBox="0 0 52 52" fill="#f0e0a8"><path d="M28 6h10v6l-4 3h-6z"/><path d="M16 20h20l-2 26H18z"/></svg></div></div>
    <h3>STEP THREE: POUR</h3>
    <p>Lorem ipsum dolor sit amet, consectetuer adipiscing elit, sed diam nonummy nibh euismod tincidunt ut laoreet dolore magna aliquam erat</p>
  </div>
</section>

<section class="keg">
  <div class="keg-photo" role="img" aria-label="Barista pulling cold brew coffee from a tap into a cup"></div>
  <div class="keg-beans" role="img" aria-label="Close-up of dark roasted coffee beans"></div>
  <div class="keg-copy">
    <div class="kicker">HOW TO KEG</div>
    <h2>COLD BREW COFFEE</h2>
    <div class="sub">For Serving Draft And Nitro Coffee</div>
    <span class="pill">One For Me</span>
  </div>
</section>

<footer class="footer">
  <div class="col" style="left:82px">
    <h4>QUICK LINKS</h4>
    <ul class="links">
      <li>HOME</li><li>ABOUT</li><li>PRODUCTS</li><li>HEALTH BENEFITS</li><li>CONTACT</li>
    </ul>
  </div>
  <div class="col" style="left:300px">
    <h4>QUICK INQUIRY</h4>
    <div class="field">Name</div>
    <div class="field">Email</div>
    <div class="field">Message</div>
    <span class="submit">SUBMIT</span>
  </div>
  <div class="col" style="left:582px;width:270px">
    <h4 style="margin-bottom:14px">CONTACT DETAILS</h4>
    <div class="contact-row"><svg width="14" height="18" viewBox="0 0 14 18"><path d="M7 0a7 7 0 0 1 7 7c0 5-7 11-7 11S0 12 0 7a7 7 0 0 1 7-7z" fill="#4a1e08"/><circle cx="7" cy="7" r="2.5" fill="#e4ddcc"/></svg><span>FERNHOLLOW COLDBREW<br>123, Lorewam Dollar almet sit ,<br>Smit Amet - 123456</span></div>
    <div class="contact-row"><svg width="14" height="14" viewBox="0 0 24 24"><path d="M6.6 10.8a15 15 0 0 0 6.6 6.6l2.2-2.2c.3-.3.7-.4 1-.2 1.1.4 2.3.6 3.6.6.6 0 1 .4 1 1V20c0 .6-.4 1-1 1A17 17 0 0 1 3 4c0-.6.4-1 1-1h3.5c.6 0 1 .4 1 1 0 1.3.2 2.5.6 3.6.1.3 0 .7-.2 1z" fill="#4a1e08"/></svg><span>555 - 018 - 2046</span></div>
    <div class="contact-row"><svg width="14" height="14" viewBox="0 0 24 24" fill="#4a1e08"><rect x="6" y="2" width="12" height="6"/><rect x="2" y="9" width="20" height="9" rx="2"/><rect x="6" y="15" width="12" height="7" fill="#e4ddcc" stroke="#4a1e08" stroke-width="2"/></svg><span>555 - 018 - 2047</span></div>
    <div class="contact-row"><svg width="14" height="14" viewBox="0 0 24 24"><rect x="2" y="5" width="20" height="14" fill="#4a1e08"/><path d="M2 5l10 8 10-8" fill="none" stroke="#e4ddcc" stroke-width="2"/></svg><span>info@fernhollowcoldbrew.com</span></div>
  </div>
  <div class="col" style="left:890px;top:50px">
    <h4>LOCATION MAP</h4>
    <div class="map" role="img" aria-label="Street map showing the location"></div>
  </div>
</footer>

<div class="copyright">
  <p>Copyright © 2016 Fernhollow Coldbrew. All Rights Reserved.</p>
  <span class="social" style="left:1048px"></span>
  <span class="social" style="left:1090px"></span>
</div>

</body>
</html>
```